Fitness competition business needs a card design

I need a professional business card design using my logo. The card will be horizontal with rounded edges.

Target Market(s)

Female fitness competitors

Industry/Entity Type

Fitness

Contact Information for Business Card

Lise-Anne Korvath
Owner
stagevelora.com
210.555.0137
info@stagevelora.com

Font styles to use
Serif

Colors

Designer to choose colors to be used in the design.

Requirements
Must have
• On the back please add the following:
• Figure
• Bikini
• Physique
• Fitness
Nice to have
• Looking for a very sleek design, contemporary and easy to read.
Should not have
• Should not be difficult to read or be too busy

```html
<!DOCTYPE html>
<html lang="en">
<head>
<meta charset="utf-8">
<title>Stage Velora – Business Card</title>
<link rel="stylesheet" href="https://fonts.googleapis.com/css2?family=EB+Garamond:wght@400;700&display=swap">
<style>
  :root {
    --backdrop-light: #c4c4c4;
    --backdrop-dark: #a9a9a9;
    --card-white: #ffffff;
    --slate: #475259;
    --text-grey: #4a555a;
    --signal-red: #ee1c25;
    --ghost: #f1f1f1;
  }
  * { margin: 0; padding: 0; box-sizing: border-box; }
  html, body { width: 1200px; height: 1200px; overflow: hidden; }
  body {
    position: relative;
    background: radial-gradient(circle at 50% 50%, var(--backdrop-light), var(--backdrop-dark));
    font-family: "EB Garamond", Georgia, serif;
  }
  .card {
    position: absolute;
    left: 218px;
    width: 764px;
    height: 462px;
    background: var(--card-white);
    overflow: hidden;
  }
  .card--front { top: 134px; border-radius: 0 48px 0 48px; }
  .card--back  { top: 606px; border-radius: 48px 0 48px 0; }
  .card__art { position: absolute; inset: 0; width: 100%; height: 100%; }

  .brand {
    position: absolute;
    left: 40px;
    top: 196px;
    width: 300px;
    display: flex;
    align-items: center;
    gap: 12px;
    justify-content: center;
  }
  .brand__dot {
    width: 38px; height: 38px; border-radius: 50%;
    background: var(--slate);
    flex: none;
  }
  .brand__name {
    font-weight: 700;
    font-size: 38px;
    letter-spacing: 1px;
    color: var(--signal-red);
    line-height: 1;
  }

  .person {
    position: absolute;
    right: 58px;
    top: 50px;
    text-align: right;
    color: var(--text-grey);
  }
  .person__name { font-size: 36px; line-height: 1; }
  .person__role { font-size: 25px; line-height: 1; margin-top: 4px; }

  .contact {
    position: absolute;
    left: 392px;
    top: 236px;
    list-style: none;
    color: var(--text-grey);
    font-size: 25px;
  }
  .contact__item { display: flex; align-items: center; gap: 10px; height: 32px; }
  .contact__item--web { margin-top: 10px; }
  .contact__icon { width: 24px; height: 24px; flex: none; }

  .disciplines {
    position: absolute;
    left: 144px;
    top: 104px;
    display: grid;
    grid-template-columns: 320px 240px;
    row-gap: 12px;
    list-style: none;
    color: var(--signal-red);
    font-weight: 700;
    font-size: 42px;
    line-height: 50px;
  }
  .disciplines__item::before {
    content: "";
    display: inline-block;
    width: 15px; height: 15px;
    border-radius: 50%;
    background: var(--signal-red);
    margin-right: 13px;
    vertical-align: 8px;
  }

  .brand--reverse {
    left: auto;
    right: 58px;
    top: 404px;
    width: auto;
    gap: 8px;
  }
  .brand--reverse .brand__dot { width: 24px; height: 24px; background: var(--card-white); }
  .brand--reverse .brand__name { font-size: 26px; color: var(--card-white); }
</style>
</head>
<body>

<section class="card card--front" aria-label="Card front">
  <svg class="card__art" viewBox="0 0 956 578" preserveAspectRatio="none" aria-hidden="true">
    <circle class="ghost-mark" cx="1000" cy="310" r="175" fill="var(--ghost)"/>
    <path class="accent-stripe" d="M100 513 L778 513 L646 530 Z" fill="var(--signal-red)"/>
    <path class="base-band" d="M0 518 L646 539 L838 513 L956 513 L956 578 L60 578 Q0 578 0 518 Z" fill="var(--slate)"/>
  </svg>

  <div class="brand">
    <span class="brand__dot"></span>
    <span class="brand__name">STAGE VELORA</span>
  </div>

  <div class="person">
    <p class="person__name">Lise-Anne Korvath</p>
    <p class="person__role">Owner</p>
  </div>

  <ul class="contact">
    <li class="contact__item">
      <svg class="contact__icon" viewBox="0 0 24 24" aria-hidden="true">
        <circle cx="12" cy="12" r="12" fill="var(--signal-red)"/>
        <path d="M6.5 14.5c2.5-4 6.5-7 11-8l-1.6 3.2-2.5.2-2.6 2.6.1 2.5-3.2 1.5z" fill="#fff"/>
      </svg>
      <span>210.555.0137</span>
    </li>
    <li class="contact__item">
      <svg class="contact__icon" viewBox="0 0 24 24" aria-hidden="true">
        <circle cx="12" cy="12" r="11" fill="none" stroke="var(--signal-red)" stroke-width="2"/>
        <rect x="6" y="8" width="12" height="8" fill="none" stroke="var(--signal-red)" stroke-width="1.6"/>
        <path d="M6 8l6 5 6-5M6 16l4.5-4M18 16l-4.5-4" fill="none" stroke="var(--signal-red)" stroke-width="1.4"/>
      </svg>
      <span>info@stagevelora.com</span>
    </li>
    <li class="contact__item contact__item--web">
      <svg class="contact__icon" viewBox="0 0 24 24" aria-hidden="true">
        <circle cx="12" cy="12" r="11" fill="none" stroke="var(--signal-red)" stroke-width="2"/>
        <ellipse cx="12" cy="12" rx="4" ry="8" fill="none" stroke="var(--signal-red)" stroke-width="1.4"/>
        <path d="M4 12h16M5.5 8h13M5.5 16h13" stroke="var(--signal-red)" stroke-width="1.4"/>
      </svg>
      <span>stagevelora.com</span>
    </li>
  </ul>
</section>

<section class="card card--back" aria-label="Card back">
  <svg class="card__art" viewBox="0 0 956 578" preserveAspectRatio="none" aria-hidden="true">
    <circle class="ghost-mark" cx="-40" cy="190" r="170" fill="var(--ghost)"/>
    <path class="accent-stripe" d="M100 386 L778 386 L646 404 Z" fill="var(--signal-red)"/>
    <path class="base-band" d="M0 394 L646 412 L838 388 L956 388 L956 518 Q956 578 896 578 L0 578 Z" fill="var(--slate)"/>
  </svg>

  <ul class="disciplines">
    <li class="disciplines__item">Figure</li>
    <li class="disciplines__item">Bikini</li>
    <li class="disciplines__item">Physique</li>
    <li class="disciplines__item">Fitness</li>
  </ul>

  <div class="brand brand--reverse">
    <span class="brand__dot"></span>
    <span class="brand__name">STAGE VELORA</span>
  </div>
</section>

</body>
</html>
```